Fresh Tarrow Work Post - Business Card Required

Dear All,

I own Velmira Limited, which in turn owns the website:
www.harbinworkpost.example

I want all of you wonderful creative people to come up with a slick, and awesome business card design that incorporates the logo on the site, and some colouring and design elements from it.

You have free reign in how you go about doing this, I won't be giving my contact details on this platform, but the winner will be asked to redesign based on my contact details which I will supply at the end.

I need the design to be completed within 5 days. I need the final print copies of the business cards by the 25th November, so unfortunately it's a bit of a rush to get these designs ready.

Any questions, please ask.

Thank you
Updates

Thank you all for your hard work and exceptional designs provided. I do have to pick one, so I have a very clear idea of which one this is, however I will wait one further day until the competition closes to be fair to all those have submitted, or are in the process of submitting. I wish you all the best and thank you again for your dedication.

```html
<!DOCTYPE html>
<html lang="en">
<head>
<meta charset="utf-8">
<title>Harbin Work Post – Business Card</title>
<link rel="stylesheet" href="https://fonts.googleapis.com/css2?family=Montserrat:wght@400;500;700&display=swap">
<style>
  :root {
    --stage: #d9d9d6;
    --card-black: #0d0d0d;
    --card-charcoal: #1c1c1c;
    --gold-deep: #a77a1c;
    --gold: #d9a93a;
    --gold-light: #f6dc8a;
    --ink: #2a1d05;
  }
  * { box-sizing: border-box; margin: 0; padding: 0; }
  html, body { width: 1200px; height: 1000px; overflow: hidden; }
  body {
    background: var(--stage);
    font-family: "Montserrat", sans-serif;
    position: relative;
  }
  .card {
    position: absolute;
    width: 600px;
    height: 343px;
    border-radius: 18px;
    overflow: hidden;
    background: radial-gradient(ellipse at 40% 60%, var(--card-charcoal), var(--card-black) 75%);
    box-shadow: 0 14px 30px rgba(0,0,0,.35);
  }
  .card--front { left: 90px; top: 110px; }
  .card--back { left: 510px; top: 545px; }

  .gold-text { color: var(--gold); }

  /* front */
  .brand-line {
    position: absolute;
    left: 40px; top: 38px;
    padding: 8px 0 6px;
    border-top: 1px solid var(--gold);
    border-bottom: 2px solid var(--gold);
  }
  .brand-name {
    font-weight: 400;
    font-size: 23px;
    letter-spacing: 2px;
    text-transform: uppercase;
    color: var(--gold);
    white-space: nowrap;
  }
  .name-band {
    position: absolute;
    left: 0; top: 96px;
    width: 600px; height: 82px;
    background: linear-gradient(90deg, var(--gold-deep), var(--gold) 30%, var(--gold-light) 55%, var(--gold) 80%, var(--gold-deep));
  }
  .person {
    position: absolute;
    left: 40px; top: 16px;
    color: var(--ink);
    white-space: nowrap;
  }
  .person__name { font-weight: 700; font-size: 24px; }
  .person__role { font-weight: 400; font-size: 14px; margin-top: 2px; }
  .band-contact {
    position: absolute;
    left: 238px; top: 18px;
    font-size: 13px;
    line-height: 1.55;
    color: var(--ink);
    white-space: nowrap;
  }
  .address {
    position: absolute;
    left: 40px; top: 218px;
    font-size: 14px;
    line-height: 1.45;
    white-space: nowrap;
  }
  .address__lines { margin-bottom: 10px; }
  .ornament-area {
    position: absolute;
    right: 0; top: 0;
    width: 118px; height: 343px;
    z-index: 1;
    background: radial-gradient(ellipse at 60% 45%, rgba(246,220,138,.55), rgba(167,122,28,.35) 45%, rgba(13,13,13,0) 75%);
  }

  /* back */
  .pattern-area {
    position: absolute;
    inset: 0;
    background: radial-gradient(ellipse at 50% 40%, #222 0%, #141414 55%, var(--card-black) 100%);
  }
  .back-brand {
    position: absolute;
    left: 0; right: 0; top: 120px;
    display: flex;
    justify-content: center;
  }
  .back-brand .brand-line { position: static; }
  .back-brand .brand-name { font-size: 26px; }
  .brand-dot {
    display: inline-block;
    width: 12px; height: 12px;
    border-radius: 50%;
    background: var(--gold);
    margin-right: 10px;
    vertical-align: middle;
  }
  .base-stripe {
    position: absolute;
    left: 0; right: 0; top: 250px;
    height: 20px;
    background: linear-gradient(90deg, var(--gold-deep), var(--gold) 30%, var(--gold-light) 55%, var(--gold) 80%, var(--gold-deep));
  }
</style>
</head>
<body>

<section class="card card--front" aria-label="Business card front">
  <div class="ornament-area" role="img" aria-label="Gold flowing swoosh ornament"></div>
  <div class="brand-line"><span class="brand-name">Harbin Work Post</span></div>
  <div class="name-band">
    <div class="person">
      <div class="person__name">Teodor Lanik</div>
      <div class="person__role">Managing Partner</div>
    </div>
    <div class="band-contact">
      teodor@harbinworkpost.example<br>
      130 555 0194
    </div>
  </div>
  <div class="address gold-text">
    <div class="address__lines">418 Marlow Ave Unit B<br>East Bramford, RI 012478</div>
    <div>T &nbsp;+30 555 0194<br>F &nbsp;+30 555 0186</div>
  </div>
</section>

<section class="card card--back" aria-label="Business card back">
  <div class="pattern-area" role="img" aria-label="Dark damask floral pattern"></div>
  <div class="back-brand">
    <div class="brand-line"><span class="brand-dot"></span><span class="brand-name">Harbin Work Post</span></div>
  </div>
  <div class="base-stripe"></div>
</section>

</body>
</html>
```